Business Card Design Project

We require business cards to be produced with the following design
http://files.brieflanter.net/art_img/38217/49302/49302_5520914_38217_image.jpg
Rather than lantern yard, please use Dolvane as the comapny name.
Please also use the following contact details:
1.
Peter Halloway
Entrepreneur
07923418870
phalloway@dolvane.net
2.
Tom Brenner
Founder
07844512039
tbrenner@dolvane.net
Please add:
Facebook favicion facebook.com/dolvane
Linked in favicon linkedin/peterhalloway
Skype favicon phalloway
Linked in favicon linkedin/thomasbrenner
Skype favicon thomasbrenner
Google Plus favicon tombrenner@maildrop.net
To the back
Industry/Entity Type
Business
Look and feel
Each slider illustrates characteristics of the customer's brand and the style your logo design should communicate.

```html
<!DOCTYPE html>
<html lang="en">
<head>
<meta charset="utf-8">
<title>Dolvane business cards</title>
<link href="https://fonts.googleapis.com/css2?family=Arimo:wght@700&family=Cabin+Condensed:wght@400;500&display=swap" rel="stylesheet">
<style>
  :root {
    --bg: #3a3a3a;
    --red: #e21d25;
    --red-dark: #a30c12;
    --red-mid: #d21a22;
    --white: #ffffff;
    --paper: #f4f4f4;
    --paper-edge: #dcdcdc;
    --ink: #333333;
    --grey: #8a8a8a;
    --rule: #9a9a9a;
  }
  * { margin: 0; padding: 0; box-sizing: border-box; }
  html, body { width: 1200px; height: 960px; overflow: hidden; }
  body { background: var(--bg); position: relative; font-family: "Cabin Condensed", sans-serif; }

  .card {
    position: absolute;
    width: 493px;
    height: 283px;
    box-shadow: 0 3px 10px rgba(0,0,0,.55);
    overflow: hidden;
  }
  .card--left { left: 84px; }
  .card--right { left: 623px; }
  .card--top { top: 169px; }
  .card--bottom { top: 543px; }

  /* front */
  .card-front {
    background: radial-gradient(ellipse at 50% 40%, var(--red) 0%, var(--red-mid) 35%, var(--red-dark) 100%);
  }
  .front-mark {
    position: absolute;
    left: 50%;
    top: 58px;
    width: 104px;
    height: 104px;
    margin-left: -52px;
    background: var(--white);
    border-radius: 22px;
  }
  .front-name {
    position: absolute;
    left: 0; right: 0;
    top: 222px;
    text-align: center;
    font-family: "Arimo", sans-serif;
    font-weight: 700;
    font-size: 22px;
    letter-spacing: .5px;
    color: var(--white);
  }

  /* back */
  .card-back {
    background: linear-gradient(180deg, var(--white) 0%, var(--paper) 60%, var(--paper-edge) 100%);
  }
  .back-mark {
    position: absolute;
    left: 59px;
    top: 66px;
    width: 92px;
    height: 92px;
    background: var(--red);
    border-radius: 20px;
  }
  .back-name {
    position: absolute;
    left: 40px;
    width: 130px;
    top: 182px;
    text-align: center;
    font-family: "Arimo", sans-serif;
    font-weight: 700;
    font-size: 15px;
    color: var(--grey);
  }
  .divider {
    position: absolute;
    left: 220px;
    top: 64px;
    width: 1px;
    height: 131px;
    background: var(--rule);
  }
  .details {
    position: absolute;
    left: 269px;
    top: 60px;
    width: 145px;
  }
  .person-name {
    font-size: 31px;
    font-weight: 500;
    color: var(--red);
    white-space: nowrap;
    line-height: 1.1;
  }
  .person-role {
    text-align: right;
    font-size: 17px;
    color: var(--ink);
    margin-top: 2px;
    white-space: nowrap;
  }
  .contact {
    list-style: none;
    margin-top: 22px;
    font-size: 17px;
    color: var(--ink);
  }
  .contact li { display: flex; align-items: center; gap: 8px; height: 27px; white-space: nowrap; }
  .contact svg { width: 12px; height: 12px; fill: var(--red); flex: none; }

  .social-band {
    position: absolute;
    left: 0; right: 0; bottom: 0;
    height: 46px;
    background: var(--red);
    display: flex;
    align-items: center;
    justify-content: space-between;
    padding: 0 26px 0 24px;
    color: var(--white);
    font-size: 14px;
  }
  .social-band--wide { padding: 0 44px 0 50px; font-size: 17px; }
  .social-item { display: flex; align-items: center; gap: 6px; white-space: nowrap; }
  .social-item::before {
    content: "";
    width: 15px; height: 15px;
    background: var(--white);
    border-radius: 2px;
    flex: none;
  }
</style>
</head>
<body>

  <section class="card card-front card--left card--top">
    <div class="front-mark"></div>
    <div class="front-name">DOLVANE</div>
  </section>

  <section class="card card-front card--right card--top">
    <div class="front-mark"></div>
    <div class="front-name">DOLVANE</div>
  </section>

  <section class="card card-back card--left card--bottom">
    <div class="back-mark"></div>
    <div class="back-name">DOLVANE</div>
    <div class="divider"></div>
    <div class="details">
      <div class="person-name">Tom Brenner</div>
      <div class="person-role">Founder</div>
      <ul class="contact">
        <li><svg viewBox="0 0 12 12"><path d="M2.5 0.5 L4.5 0.5 L5 3.5 L3.6 4.6 Q4.8 7.2 7.4 8.4 L8.5 7 L11.5 7.5 L11.5 9.5 Q11 11.5 9 11.5 Q0.5 10.5 0.5 3 Q0.5 1 2.5 0.5 Z"/></svg>07844512039</li>
        <li><svg viewBox="0 0 12 12"><path d="M0 2 H12 V10 H0 Z M0.8 2.8 L6 6.6 L11.2 2.8" fill="var(--red)"/><path d="M1 2.6 L6 6.2 L11 2.6" fill="none" stroke="#fff" stroke-width="1"/></svg>tbrenner@dolvane.net</li>
      </ul>
    </div>
    <div class="social-band">
      <span class="social-item">/dolvane</span>
      <span class="social-item">/thomasbrenner</span>
      <span class="social-item">thomasbrenner</span>
      <span class="social-item">tombrenner@maildrop.net</span>
    </div>
  </section>

  <section class="card card-back card--right card--bottom">
    <div class="back-mark"></div>
    <div class="back-name">DOLVANE</div>
    <div class="divider"></div>
    <div class="details">
      <div class="person-name">Peter Halloway</div>
      <div class="person-role">Entrepreneur</div>
      <ul class="contact">
        <li><svg viewBox="0 0 12 12"><path d="M2.5 0.5 L4.5 0.5 L5 3.5 L3.6 4.6 Q4.8 7.2 7.4 8.4 L8.5 7 L11.5 7.5 L11.5 9.5 Q11 11.5 9 11.5 Q0.5 10.5 0.5 3 Q0.5 1 2.5 0.5 Z"/></svg>07923418870</li>
        <li><svg viewBox="0 0 12 12"><path d="M0 2 H12 V10 H0 Z" fill="var(--red)"/><path d="M1 2.6 L6 6.2 L11 2.6" fill="none" stroke="#fff" stroke-width="1"/></svg>phalloway@dolvane.net</li>
      </ul>
    </div>
    <div class="social-band social-band--wide">
      <span class="social-item">/dolvane</span>
      <span class="social-item">/peterhalloway</span>
      <span class="social-item">phalloway</span>
    </div>
  </section>

</body>
</html>
```